4 Icons needed for Eyecare Website (fun project)

We need 4 updated icons for an optometry practice.

URL is www.pinecrestopticare.example

1st icon- schedule an appointment
2nd, 3rd, 4th and 5th icons - right side of the page under an eye on the future. They will be for Order Contacts, Optical Gallery, Contact Lens Care and Meet the doctors (see attache image)
Updates

Reason: I will be out of the country until the 12th of November so the contest will end then Thanks All Darby

Target Market(s)

consumer

Industry/Entity Type

Optician

Font styles to use
Serif

Requirements
Must have
• Check out http://www.wendlevision.example for other examples.
• For the schedule an appointment button just have schedule an appointment and use the image from Steamboat Springs Colorado. - http://www.quillfeatherlodge.example you can use the barn image then overlay text that says schedule an appointment.
• - on the others the only requirement is to have an image of both docs on the meet the docs icon
Nice to have
• ad pinecrest opticare logo to schedule an appointment icon
Should not have
• no black and white would like some color to the site

```html
<!DOCTYPE html>
<html lang="en">
<head>
<meta charset="utf-8">
<title>Pinecrest Opticare — Icons</title>
<link rel="stylesheet" href="https://fonts.googleapis.com/css2?family=Bitter:wght@400;700&family=Zilla+Slab:wght@400&display=swap">
<style>
  :root {
    --page: #ffffff;
    --ink: #2e2f33;
    --cta: #0b1a12;
    --cta-text: #ffffff;
    --accent: #4b9ccb;
    --panel-top: #040806;
    --panel-bottom: #22393f;
    --snow: #eef3f5;
    --snow-shade: #d5dfe4;
    --snow-mint: #cde4dc;
    --barn: #6b5a4c;
    --barn-dark: #4d4038;
  }
  * { box-sizing: border-box; margin: 0; padding: 0; }
  html, body { width: 1200px; height: 1200px; overflow: hidden; background: var(--page); }
  .canvas { position: relative; width: 1200px; height: 1200px; }

  .banner {
    position: absolute; left: 33px; top: 32px; width: 1135px; height: 296px;
    overflow: hidden;
  }
  .banner-photo {
    position: absolute; inset: 0;
    background:
      linear-gradient(180deg, rgba(238,243,245,0) 0%, rgba(238,243,245,0) 74%, var(--snow) 84%, var(--snow-shade) 100%),
      radial-gradient(ellipse 180px 70px at 300px 210px, rgba(77,64,56,0.85), rgba(77,64,56,0) 100%),
      radial-gradient(ellipse 210px 60px at 770px 225px, rgba(107,90,76,0.95), rgba(107,90,76,0) 100%),
      radial-gradient(ellipse 170px 50px at 560px 195px, rgba(107,90,76,0.8), rgba(107,90,76,0) 100%),
      radial-gradient(ellipse 260px 90px at 330px 70px, rgba(245,248,250,0.95), rgba(245,248,250,0) 100%),
      linear-gradient(180deg, #aebcbd 0%, #c9d2d3 35%, #b7bcb9 60%, #dfe6e8 80%),
      linear-gradient(90deg, var(--snow-mint) 0%, rgba(205,228,220,0) 35%);
    background-blend-mode: normal;
  }
  .banner-photo::after {
    content: ""; position: absolute; inset: 0;
    background: linear-gradient(90deg, rgba(205,228,220,0.55) 0%, rgba(205,228,220,0) 40%, rgba(120,160,160,0.25) 100%);
  }
  .brand {
    position: absolute; left: 72px; top: 108px; width: 296px; text-align: center;
    font-family: 'Bitter', serif; color: var(--ink);
  }
  .brand-name { font-size: 28px; font-weight: 700; line-height: 1.1; }
  .brand-tagline { font-size: 9px; font-weight: 700; margin-top: 6px; line-height: 1.1; text-transform: uppercase; }

  .headline-box {
    position: absolute; left: 369px; top: 14px; right: 0; height: 132px;
    background: #fff; border: 4px solid #3a3b40; border-right: none;
    display: flex; align-items: center; justify-content: center; text-align: center;
    font-family: 'Bitter', serif; font-weight: 700; font-size: 36px; line-height: 1.27;
    color: var(--ink);
  }
  .cta {
    position: absolute; left: 818px; top: 149px; right: 0; height: 42px;
    background: var(--cta); color: var(--cta-text);
    font-family: 'Zilla Slab', serif; font-size: 25px;
    display: flex; align-items: center; justify-content: center;
  }

  .feature-panel {
    position: absolute; left: 362px; top: 379px; width: 476px; height: 771px;
    background: linear-gradient(180deg, var(--panel-top) 0%, var(--panel-top) 60%, var(--panel-bottom) 100%);
  }
  .panel-title {
    position: absolute; left: 21px; top: 30px; width: 308px;
    font-family: Helvetica, Arial, sans-serif; font-weight: 400; font-size: 29px; color: var(--accent);
    padding-bottom: 4px; border-bottom: 2px solid var(--accent);
  }
  .tile { position: absolute; left: 20px; width: 436px; height: 149px; overflow: hidden; }
  .tile-photo { position: absolute; inset: 0; }
  .tile-label {
    position: absolute; left: 22px; height: 37px; padding: 0 8px;
    background: #fff; border: 2px solid var(--accent); color: var(--accent);
    font-family: 'Zilla Slab', serif; font-size: 20px;
    display: flex; align-items: center; white-space: nowrap;
  }

  .tile-contacts { top: 95px; }
  .tile-contacts .tile-photo {
    background:
      radial-gradient(ellipse 80px 40px at 165px 88px, rgba(120,200,220,0.75), rgba(180,225,232,0.35) 60%, rgba(255,255,255,0) 100%),
      radial-gradient(ellipse 78px 46px at 296px 66px, rgba(110,190,215,0.7), rgba(190,228,235,0.35) 60%, rgba(255,255,255,0) 100%),
      radial-gradient(ellipse 150px 14px at 200px 118px, rgba(170,220,170,0.45), rgba(255,255,255,0) 100%),
      linear-gradient(90deg, #f4f3ef, #f8f8f5 50%, #f6f5f1);
  }
  .tile-gallery { top: 259px; }
  .tile-gallery .tile-photo {
    background:
      linear-gradient(160deg, rgba(0,0,0,0) 22%, rgba(122,84,52,0.9) 28%, rgba(150,110,70,0.6) 33%, rgba(0,0,0,0) 40%),
      linear-gradient(160deg, rgba(0,0,0,0) 50%, rgba(110,75,45,0.85) 56%, rgba(140,100,65,0.5) 61%, rgba(0,0,0,0) 67%),
      linear-gradient(160deg, rgba(0,0,0,0) 72%, rgba(70,60,60,0.6) 77%, rgba(0,0,0,0) 83%),
      linear-gradient(90deg, #dfe6ea 0%, #b8c6cf 35%, #98aab6 65%, #cdd6dc 100%);
  }
  .tile-care { top: 421px; }
  .tile-care .tile-photo {
    background:
      radial-gradient(ellipse 120px 42px at 290px 68px, rgba(70,170,200,0.85), rgba(120,200,220,0.5) 55%, rgba(200,235,240,0) 100%),
      radial-gradient(ellipse 110px 60px at 260px 160px, rgba(235,205,195,0.95), rgba(240,220,212,0.6) 55%, rgba(220,238,240,0) 100%),
      linear-gradient(180deg, #b6dde3 0%, #cfe8ec 55%, #dcecee 100%);
  }
  .tile-doctors { top: 583px; }
  .tile-doctors .tile-photo {
    background:
      radial-gradient(ellipse 70px 90px at 50px 100px, rgba(150,130,120,0.8), rgba(150,130,120,0) 100%),
      radial-gradient(ellipse 90px 60px at 230px 70px, rgba(255,255,255,0.95), rgba(255,255,255,0) 100%),
      radial-gradient(ellipse 22px 22px at 225px 80px, rgba(40,40,45,0.85), rgba(40,40,45,0) 100%),
      radial-gradient(ellipse 22px 22px at 262px 80px, rgba(40,40,45,0.85), rgba(40,40,45,0) 100%),
      radial-gradient(ellipse 80px 100px at 400px 60px, rgba(120,90,70,0.85), rgba(120,90,70,0) 100%),
      linear-gradient(90deg, #8f989d 0%, #c9cfd2 30%, #eef0f1 55%, #e4e7e8 80%, #cfd3d5 100%);
  }
</style>
</head>
<body>
<main class="canvas">
  <section class="banner">
    <div class="banner-photo" role="img" aria-label="Snow-covered wooden barns in a winter mountain valley"></div>
    <div class="brand">
      <div class="brand-name">Pinecrest Opticare</div>
      <div class="brand-tagline">Exclusive eyewear,<br>quality eyecare</div>
    </div>
    <h1 class="headline-box">Full - SPECTRUM VISION CARE FOR YOU<br>AND YOUR FAMILY</h1>
    <div class="cta">- Schedule an Appointment -</div>
  </section>

  <section class="feature-panel">
    <h2 class="panel-title">An eye on the Future</h2>

    <div class="tile tile-contacts">
      <div class="tile-photo" role="img" aria-label="Two soft contact lenses on a light background"></div>
      <div class="tile-label" style="top:43px;">Order Contacts</div>
    </div>
    <div class="tile tile-gallery">
      <div class="tile-photo" role="img" aria-label="Tortoiseshell and clear eyeglass frames laid out together"></div>
      <div class="tile-label" style="top:54px;">Optical Gallery</div>
    </div>
    <div class="tile tile-care">
      <div class="tile-photo" role="img" aria-label="A blue contact lens balanced on a fingertip"></div>
      <div class="tile-label" style="top:52px;">Contact Lens Care</div>
    </div>
    <div class="tile tile-doctors">
      <div class="tile-photo" role="img" aria-label="An eye doctor examining a patient with a slit lamp"></div>
      <div class="tile-label" style="top:52px;">Meet the Doctors</div>
    </div>
  </section>
</main>
</body>
</html>
```